Tovrelan Ltda

Logo design focused on: - Construction of civil works - Electrical services - Metal structures - Equipment rental Tomás Ibarra Leiva Manager tovrelan.ltda@brevomail.example 56 9 48215037 Quelitoco s / n, Sorimar, San Pedro de Atacama

Building

Colors
33a6d7
0292cd
33b8a4
0555a3

```html
<!DOCTYPE html>
<html lang="es">
<head>
<meta charset="utf-8">
<title>Tovrelan Ltda — Business Card</title>
<link rel="stylesheet" href="https://fonts.googleapis.com/css2?family=Fira+Sans:wght@400;500&family=Work+Sans:wght@400;500&display=swap">
<style>
  :root {
    --page-bg: #1d1d1d;
    --card-white: #ffffff;
    --brand-blue: #0555a3;
    --brand-mid: #1277bf;
    --brand-sky: #33a6d7;
    --brand-teal: #33b8a4;
    --brand-cyan: #0292cd;
    --text-dark: #3d3d3d;
  }
  * { margin: 0; padding: 0; box-sizing: border-box; }
  html, body { width: 1200px; height: 897px; overflow: hidden; background: var(--page-bg); }
  body { position: relative; font-family: "Work Sans", Arial, sans-serif; }

  .card {
    position: absolute;
    left: 303px;
    width: 595px;
    height: 338px;
    border-radius: 20px;
    overflow: hidden;
  }
  .card--front { top: 92px; background: var(--card-white); }
  .card--back { top: 469px; background: var(--brand-mid); }

  .brand {
    position: absolute;
    display: flex;
    align-items: center;
    gap: 10px;
  }
  .brand__dot {
    width: 50px; height: 50px; border-radius: 50%;
    background: var(--brand-cyan);
  }
  .brand__name {
    font-family: "Work Sans", Arial, sans-serif;
    font-weight: 500;
    font-size: 30px;
    letter-spacing: 0.5px;
    color: var(--brand-blue);
    white-space: nowrap;
  }
  .card--front .brand { left: 33px; top: 35px; }
  .card--back .brand { left: 50%; top: 142px; transform: translateX(-50%); }
  .card--back .brand__dot { background: var(--brand-teal); }
  .card--back .brand__name { color: var(--card-white); font-size: 34px; }

  .services {
    position: absolute;
    right: 33px; top: 47px;
    list-style: none;
    text-align: right;
    font-family: "Fira Sans", Arial, sans-serif;
    font-size: 14px;
    line-height: 19px;
  }
  .services li:nth-child(odd) { color: var(--brand-blue); }
  .services li:nth-child(even) { color: var(--brand-cyan); }

  .address {
    position: absolute;
    left: 28px; top: 189px;
    font-size: 13.5px; line-height: 17.5px;
    color: var(--text-dark);
    font-style: normal;
  }
  .person {
    position: absolute;
    right: 32px; top: 181px;
    text-align: right;
    font-family: "Fira Sans", Arial, sans-serif;
  }
  .person__name { font-size: 20px; font-weight: 400; letter-spacing: 1.4px; color: var(--brand-blue); }
  .person__role { font-size: 14px; letter-spacing: 0.6px; color: var(--text-dark); margin-top: 2px; }

  .divider {
    position: absolute;
    left: 29px; right: 33px; top: 238px;
    height: 1.5px; background: var(--brand-cyan);
  }
  .contacts {
    position: absolute;
    left: 29px; top: 249px;
    list-style: none;
    font-size: 13.5px; line-height: 17.5px;
    color: var(--text-dark);
  }
  .contacts li { display: flex; align-items: center; gap: 9px; }
  .contacts svg { width: 9px; height: 9px; flex: none; }

  .wave { position: absolute; left: 0; bottom: 0; width: 595px; height: 50px; }

  .site {
    position: absolute;
    left: 0; right: 0; top: 300px;
    text-align: center;
    font-size: 14px;
    color: var(--card-white);
  }
</style>
</head>
<body>

<section class="card card--front">
  <div class="brand">
    <span class="brand__dot"></span>
    <span class="brand__name">TOVRELAN Ltda</span>
  </div>

  <ul class="services">
    <li>Construccion de OO. CC.</li>
    <li>Estructuras Metalicas</li>
    <li>Servicios Electricos</li>
    <li>Arriendo de Equipos</li>
  </ul>

  <address class="address">Quelitoco s / n, Sorimar,<br>San Pedro de Atacama</address>

  <div class="person">
    <p class="person__name">TOMÁS IBARRA LEIVA</p>
    <p class="person__role">Manager</p>
  </div>

  <div class="divider"></div>

  <ul class="contacts">
    <li>
      <svg viewBox="0 0 10 10"><path d="M2 1 L4 1 L4.6 3 L3.5 3.8 Q4.5 5.8 6.2 6.5 L7 5.4 L9 6 L9 8 Q8.5 9 7.5 9 Q2 8 1 2.5 Q1 1.5 2 1 Z" fill="var(--brand-blue)"/></svg>
      56 9 48215037
    </li>
    <li>
      <svg viewBox="0 0 10 10"><rect x="0.8" y="2" width="8.4" height="6" fill="none" stroke="var(--brand-blue)" stroke-width="1.2"/><path d="M1 2.3 L5 5.3 L9 2.3" fill="none" stroke="var(--brand-blue)" stroke-width="1.1"/></svg>
      tovrelan.ltda@brevomail.example
    </li>
    <li>
      <svg viewBox="0 0 10 10"><circle cx="5" cy="5" r="4" fill="none" stroke="var(--brand-blue)" stroke-width="1"/><ellipse cx="5" cy="5" rx="1.8" ry="4" fill="none" stroke="var(--brand-blue)" stroke-width="0.8"/><path d="M1 5 H9" stroke="var(--brand-blue)" stroke-width="0.8"/></svg>
      www.tovrelan.ltda
    </li>
  </ul>

  <svg class="wave" viewBox="0 0 595 50" preserveAspectRatio="none" aria-hidden="true">
    <path d="M193 50 Q380 -6 595 8 L595 50 Z" fill="var(--brand-teal)"/>
    <path d="M268 50 Q420 10 595 14 L595 50 Z" fill="var(--card-white)"/>
    <path d="M274 50 Q425 14 595 17 L595 50 Z" fill="var(--brand-mid)"/>
  </svg>
</section>

<section class="card card--back">
  <div class="brand">
    <span class="brand__dot"></span>
    <span class="brand__name">TOVRELAN Ltda</span>
  </div>
  <p class="site">www.tovrelan.ltda</p>
</section>

</body>
</html>
```